Road Sign at our office 84 in X 48 in - Small Billboard

Kestrel Electrical
Electrical & Lighting Services

- we need a sign design for our small business/company based in Calhoun, GA called Kestrel Electrical - "our mission is to provide Northwest Georgia with dependable, high-quality electrical services that prioritize safety, integrity, and long-term reliability. As a woman-owned business with over 25 years of experience, we are committed to delivering exceptional workmanship and personalized service for every commercial, residential, and industrial project we undertake. We stand behind our work with a lifetime warranty—because your trust is our most powerful connection."

display logo, phone number, and open to other ideas without being cluttered, maybe instead of full website address, just use @kstelectrical and it will send them to all of our website and socials...

it needs to be easy to read as they drive down the road
this is a place where people may be traveling at high speeds, make sure it's easy to see and understand at a glance.
It will be hanging 20-24ft from the ground. Like a small billboard.

https://kstelectricalservices.example/

Industry/Entity Type

Electrical Contractor

Requirements
Nice to have
• match the look and feel of website and socials

```html
<!DOCTYPE html>
<html lang="en">
<head>
<meta charset="utf-8">
<title>Kestrel Electrical – Road Sign</title>
<link href="https://fonts.googleapis.com/css2?family=Montserrat:wght@600;700&display=swap" rel="stylesheet">
<style>
  :root {
    --backdrop: #e8ecf1;
    --sign-white: #ffffff;
    --ink: #231f20;
    --flame-orange: #f39419;
    --signal-red: #e53935;
    --light: #ffffff;
  }
  * { box-sizing: border-box; margin: 0; padding: 0; }
  html, body {
    width: 1200px; height: 802px; overflow: hidden;
    background: var(--backdrop);
    font-family: "Montserrat", Arial, sans-serif;
  }
  .sign {
    position: absolute; left: 40px; top: 81px;
    width: 1120px; height: 640px;
    background: var(--sign-white);
    overflow: hidden;
    box-shadow: 0 6px 24px rgba(0,0,0,0.15);
  }
  .handle-pill {
    position: absolute; right: 36px; top: 34px;
    height: 104px; padding: 0 50px;
    border-radius: 52px;
    background: var(--flame-orange);
    color: var(--ink);
    font-weight: 700; font-size: 62px; line-height: 104px;
    letter-spacing: 0.5px;
  }
  .brand {
    position: absolute; left: 56px; top: 176px;
    display: flex; align-items: center; gap: 40px;
  }
  .brand-dot {
    width: 240px; height: 240px; border-radius: 50%;
    background: var(--flame-orange);
    flex: none;
  }
  .brand-name {
    color: var(--ink);
    font-weight: 700; font-size: 108px; line-height: 1.02;
    letter-spacing: -1px;
  }
  .call-band {
    position: absolute; left: 0; right: 0; bottom: 0;
    height: 164px;
    background: var(--signal-red);
    display: flex; align-items: center; justify-content: center; gap: 28px;
  }
  .call-label {
    color: var(--ink);
    font-weight: 700; font-size: 46px; line-height: 1.0;
  }
  .call-number {
    color: var(--light);
    font-weight: 600; font-size: 112px; line-height: 1;
    letter-spacing: 1px;
  }
</style>
</head>
<body>
  <main class="sign">
    <div class="handle-pill">@kstelectrical</div>

    <div class="brand">
      <div class="brand-dot"></div>
      <div class="brand-name">Kestrel<br>Electrical</div>
    </div>

    <div class="call-band">
      <div class="call-label">Call<br>Now</div>
      <div class="call-number">706-555-0142</div>
    </div>
  </main>
</body>
</html>
```